Car Repair Business Website Redesign

We need a new design for our wordpress website, which generates traffic and converts leads for our car repair business. The site was originally setup with a blank template and the design was never tweaked. All content is in place, so the design needs to arrange existing content into a visually strong, responsive layout with top priority given to conversion. You can view the existing website at www.brightlanegarageworks.com. Responsive design is extremely important - 36% of visitors are mobile and 18% tablet - so please include mobile designs.
To confirm, the brief is for PSD only, please supply designs for the following two pages:-
http://www.brightlanegarageworks.com/
http://www.brightlanegarageworks.com/clutch-replacement/
Target Market(s)
Predominantly male (75%), 25-55 year old (70%) audience.
Industry/Entity Type
Car Repair
Number of Pages Required
2 page
Font styles to use
Requirements
Must have
- Good use of colour, clear design elements. Our competitors just had a re-design which although not perfect, displays many good elements: www.gearvalet.com

```html
<!DOCTYPE html>
<html lang="en">
<head>
<meta charset="utf-8">
<title>Brightlane Garage Works</title>
<link href="https://fonts.googleapis.com/css2?family=Arimo:wght@400;700&family=Roboto:wght@300;400&display=swap" rel="stylesheet">
<style>
:root{
  --navy:#1d3557;
  --navy-deep:#15294a;
  --white:#ffffff;
  --ink:#1a1a1a;
  --grey-bg:#e9ebf1;
  --orange:#e8622a;
  --orange-dark:#c9541f;
  --green:#39d353;
  --circle:#25206b;
  --sky:#a9c6ec;
}
*{margin:0;padding:0;box-sizing:border-box}
html,body{width:1200px;height:2311px;overflow:hidden}
body{position:relative;background:var(--white);font-family:"Arimo",Arial,sans-serif;color:var(--ink)}
.abs{position:absolute}

/* header */
.site-header{left:0;top:0;width:1200px;height:116px;background:var(--white)}
.header-decor{left:0;top:0;width:240px;height:116px;background:linear-gradient(120deg,var(--navy) 0%,#5d6f8c 55%,var(--white) 100%)}
.brand{left:0;width:1200px;top:42px;text-align:center;font-weight:700;font-size:30px;color:var(--navy-deep)}
.brand-dot{display:inline-block;width:12px;height:12px;border-radius:50%;background:var(--navy-deep);margin-right:10px;vertical-align:middle}
.header-phone{right:24px;top:36px;text-align:right;font-size:20px;line-height:31px}

/* nav */
.main-nav{left:0;top:116px;width:1200px;height:44px;background:var(--navy);display:flex;align-items:center;padding-left:40px}
.main-nav a{color:var(--white);text-decoration:none;font-weight:700;font-size:17px;letter-spacing:.6px;margin-right:46px}

/* hero */
.hero{left:0;top:160px;width:1200px;height:445px;background:linear-gradient(110deg,#6e7680 0%,#8d9aa4 25%,#2b3a78 50%,#233066 70%,#59616b 100%)}
.hero-intro{left:54px;top:181px;width:336px;height:248px;background:rgba(255,255,255,.72);border-radius:14px;padding:16px 10px 0 10px;font-weight:700;font-size:19.5px;line-height:29px;letter-spacing:.4px}
.hero-cta{left:0;top:449px;width:458px;height:129px;background:rgba(21,41,74,.94);border-radius:0 12px 12px 0;color:var(--white);text-align:center;font-weight:700}
.hero-cta h2{font-size:22px;letter-spacing:1px;margin-top:14px}
.hero-cta p{font-size:17px;line-height:22px;margin-top:18px}
.hero-cta .hl{color:var(--green)}

/* services */
.service{width:250px;text-align:center}
.service h3{font-family:"Roboto",Arial,sans-serif;font-weight:400;font-size:27px;line-height:36px;letter-spacing:1.5px;height:100px}
.service-art{width:178px;height:178px;border-radius:50%;border:4px solid var(--circle);margin:0 auto;padding:8px;background:var(--white)}
.service-art div{width:100%;height:100%;border-radius:50%}
.service p{font-size:15.5px;line-height:25px;text-align:left;margin:32px 0 0 22px;width:214px;height:122px;hyphens:auto}
.btn{display:inline-block;background:var(--navy);color:var(--white);font-size:14px;border-radius:18px;padding:9px 22px;text-decoration:none}

/* info band */
.info-band{left:0;top:1194px;width:1200px;height:719px;background:var(--grey-bg)}
.section-title{font-family:"Roboto",Arial,sans-serif;font-weight:400;font-size:27px;letter-spacing:1.2px}
.founder-photo{left:135px;top:1275px;width:116px;height:136px;background:linear-gradient(180deg,#9fb4c6,#3f4a55)}
.founder-quote{left:265px;top:1275px;width:305px;font-size:19px;line-height:27px}
.faq-list{left:135px;top:1538px;list-style:none;font-size:16px;line-height:29px;width:460px}
.faq-list li{position:relative;padding-left:32px}
.faq-list li::before{content:"";position:absolute;left:4px;top:9px;width:13px;height:13px;border-radius:50%;background:var(--orange-dark)}

.rating-badge{left:726px;top:1225px;width:354px;height:78px;display:flex}
.rating-left{width:213px;background:var(--orange);color:var(--white);text-align:center;padding-top:6px}
.rating-left span{font-size:20px;letter-spacing:1px}
.rating-right{flex:1;background:var(--orange-dark);color:var(--white);padding:12px 0 0 16px;font-size:18px;line-height:27px;font-weight:700}
.review{left:726px;width:346px}
.review-head{background:var(--white);height:40px;display:flex;justify-content:space-between;align-items:center;padding:0 12px 0 4px}
.review-name{color:var(--orange);font-size:20px}
.review-text{font-size:15px;line-height:27px;padding-top:6px;height:120px;overflow:hidden}
.more{position:absolute;right:8px;background:var(--orange-dark);color:var(--white);font-size:13px;border-radius:12px;padding:3px 12px}

/* map + contact */
.map-area{left:0;top:1913px;width:1200px;height:190px;background:linear-gradient(90deg,#c7d6b8,#dfe6d4 50%,#cfdcec)}
.contact{left:0;top:2103px;width:1200px;height:208px;background:var(--sky);text-align:center}
.contact h2{font-family:"Roboto",Arial,sans-serif;font-weight:400;font-size:27px;letter-spacing:1.5px;margin-top:22px}
.contact-cols{display:flex;justify-content:center;gap:22px;font-size:15px;line-height:22px;margin-top:8px}
.legal{font-size:11.5px;line-height:15px;margin-top:30px}
</style>
</head>
<body>

<header class="site-header abs">
  <div class="header-decor abs" role="img" aria-label="Decorative navy corner band"></div>
  <div class="brand abs"><span class="brand-dot"></span>Brightlane Garage Works</div>
  <div class="header-phone abs">0330 555 0142<br>*Free from Mobiles and Landlines</div>
</header>

<nav class="main-nav abs">
  <a href="#">HOME</a><a href="#">ABOUT US</a><a href="#">CLUTCH REPLACEMENT</a><a href="#">CAMBELT REPLACEMENT</a><a href="#">SERVICING</a><a href="#">BRAKE DISCS &amp; PADS</a>
</nav>

<section class="hero abs" role="img" aria-label="Rear view of a blue sports car with white racing stripes on a race track"></section>
<div class="hero-intro abs">Brightlane Garage Works offer convenient and affordable motoring. We offer a range of services at fixed prices – either on-site at work or home, or at one of our workshops with free collection and delivery.</div>
<div class="hero-cta abs">
  <h2>Do I Need a Clutch Replacement?</h2>
  <p>Just answer a few basic questions to diagnose<br>your clutch problem with our<br><span class="hl">interactive clutch troubleshooter!</span></p>
</div>

<div class="service abs" style="left:110px;top:673px">
  <h3>CLUTCH<br>REPLACEMENT</h3>
  <div class="service-art"><div role="img" aria-label="Clutch plate and pressure plate" style="background:linear-gradient(160deg,#c9ccd2,#6b7079)"></div></div>
  <p lang="en">As clutch specialists replacing hundreds of clutches every month, we offer convenience, reliability and value.</p>
  <a class="btn" href="#">READ MORE</a>
</div>
<div class="service abs" style="left:368px;top:673px">
  <h3>CAMBELT<br>REPLACEMENT</h3>
  <div class="service-art"><div role="img" aria-label="Toothed timing belt" style="background:linear-gradient(160deg,#8a8a8a,#3a3a3a)"></div></div>
  <p lang="en">Keeping to your scheduled cambelt (or "timing belt") changes is vital in order to avoid an expensive repair bill.</p>
  <a class="btn" href="#">READ MORE</a>
</div>
<div class="service abs" style="left:603px;top:673px">
  <h3>SERVICING<br>&nbsp;</h3>
  <div class="service-art"><div role="img" aria-label="Mechanic working on an engine" style="background:linear-gradient(160deg,#b0b8c8,#2f3f8f)"></div></div>
  <p lang="en">Not only can we service your car on-site, but we use original manufacturer parts at a fraction of the cost of the main dealer.</p>
  <a class="btn" href="#">READ MORE</a>
</div>
<div class="service abs" style="left:853px;top:673px">
  <h3>BRAKE<br>DISCS &amp; PADS</h3>
  <div class="service-art"><div role="img" aria-label="Brake disc and caliper" style="background:linear-gradient(160deg,#e2e4e8,#8a8f98)"></div></div>
  <p lang="en">We recommend fitting premium quality Stoprite Brake Discs and Brake Pads, for better performance and extra safety.</p>
  <a class="btn" href="#">READ MORE</a>
</div>

<section class="info-band abs"></section>
<h2 class="section-title abs" style="left:135px;top:1216px">A Few Words From Our Founder...</h2>
<div class="founder-photo abs" role="img" aria-label="Portrait of the company founder"></div>
<div class="founder-quote abs">"I was fed-up of being messed around by garages! All I wanted was somewhere I could take my car that I could trust not to rip me off, offered good..."</div>
<a class="btn abs" href="#" style="left:468px;top:1410px;padding:6px 14px;font-size:15px">Read more</a>

<h2 class="section-title abs" style="left:135px;top:1480px">Clutch Frequently Asked Questions</h2>
<ul class="faq-list abs">
  <li>How do I know if I need a Clutch Replacement?</li>
  <li>How quickly can you get my car booked in for a clutch replacement?</li>
  <li>How long does it take to get my clutch repaired?</li>
  <li>There is further work required on my vehicle, are you able to help?</li>
  <li>My car is an automatic, is it fitted with a clutch?</li>
  <li>How can I pay for my clutch repair?</li>
  <li>How does the warranty work?</li>
</ul>

<div class="rating-badge abs">
  <div class="rating-left"><span>EXCELLENT</span>
    <svg width="200" height="40" viewBox="0 0 200 40" aria-hidden="true"><g fill="var(--white)">
      <polygon id="st" points="20,4 24.7,15 36,15 27,22 30.5,34 20,27 9.5,34 13,22 4,15 15.3,15"/>
      <use href="#st" x="38"/><use href="#st" x="76"/><use href="#st" x="114"/><use href="#st" x="152"/></g></svg>
  </div>
  <div class="rating-right">4.9 Average<br>198 Reviews</div>
</div>

<div class="review abs" style="top:1318px">
  <div class="review-head"><span class="review-name">Daniel Ashworth</span>
    <svg width="130" height="22" viewBox="0 0 130 22" aria-hidden="true"><g fill="var(--orange)"><polygon id="rs" points="11,1 13.6,8 21,8 15,12.5 17.3,20 11,15.5 4.7,20 7,12.5 1,8 8.4,8"/><use href="#rs" x="27"/><use href="#rs" x="54"/><use href="#rs" x="81"/><use href="#rs" x="108"/></g></svg></div>
  <div class="review-text">man arrived as agreed time very courteous offered some advice, drove my car, left his, said tomorrow afternoon we went out for forty minutes after lunch the next day arrived back home to find car on th</div>
  <span class="more" style="top:156px">more</span>
</div>
<div class="review abs" style="top:1508px">
  <div class="review-head"><span class="review-name">Karen Lister</span>
    <svg width="130" height="22" viewBox="0 0 130 22" aria-hidden="true"><g fill="var(--orange)"><use href="#rs"/><use href="#rs" x="27"/><use href="#rs" x="54"/><use href="#rs" x="81"/><use href="#rs" x="108"/></g></svg></div>
  <div class="review-text">What a service!!! Called Tuesday, booked for a full clutch replacement, my car was picked up Thursday morning (today) and I have it back Thursday evening! Fantastic service throughout, listened,</div>
  <span class="more" style="top:156px">more</span>
</div>
<div class="review abs" style="top:1700px">
  <div class="review-head"><span class="review-name">Paula Merrick</span>
    <svg width="130" height="22" viewBox="0 0 130 22" aria-hidden="true"><g fill="var(--orange)"><use href="#rs"/><use href="#rs" x="27"/><use href="#rs" x="54"/><use href="#rs" x="81"/><use href="#rs" x="108"/></g></svg></div>
  <div class="review-text" style="padding-top:14px;height:126px">Was so easy dealing with this company. Was great to have the car picked up and brought back to my house. Also was easy to give card details over the phone, thus eliminating the</div>
  <span class="more" style="top:164px">more</span>
</div>

<div class="map-area abs" role="img" aria-label="Map of southern England with workshop location markers"></div>

<footer class="contact abs">
  <h2>CONTACT US</h2>
  <div class="contact-cols">
    <div style="text-align:right">Need advice? Got a question?<br>Calls us on 0800 555 0199</div>
    <div style="text-align:left">You can also email us at:<br>info@brightlanegarageworks.com</div>
  </div>
  <div class="legal">*Free calls - 0330 is a local rate number, meaning that calls will be included in call packages for both mobile phones and landlines<br>
  © 2015 Brightlane Garage Works: Regional Clutch and Servicing Specialists. All Rights Reserved.<br>
  Brightlane Garage Works is rated 4.89 stars by ReviewPoint based on 196 reviews<br>
  Brightlane Garage Works is a registered company in England &amp; Wales, registration number 7418830. Registered Office: 14 Harbour Row, Portsmouth, Hampshire, PO1 3LJ</div>
</footer>

</body>
</html>
```